BRVO Membership Certificate

We are launching an online membership for www.brvo.com

When someone joins they will receive a membership certificate that outlines their name, membership number, membership status, date of membership

```html
<!DOCTYPE html>
<html lang="en">
<head>
<meta charset="utf-8">
<title>BRVO Membership Certificate</title>
<link href="https://fonts.googleapis.com/css2?family=Manrope:wght@300;400;500;700;800&display=swap" rel="stylesheet">
<style>
  :root {
    --navy: #27316a;
    --gold: #f0d048;
    --paper: #ffffff;
    --ink-light: #ffffff;
    --rule: rgba(255, 255, 255, 0.75);
  }
  html, body {
    margin: 0;
    padding: 0;
    width: 848px;
    height: 1200px;
    overflow: hidden;
    background: var(--paper);
  }
  .certificate {
    position: relative;
    width: 848px;
    height: 1200px;
    background: var(--paper);
    font-family: "Manrope", sans-serif;
    color: var(--ink-light);
    overflow: hidden;
  }
  .certificate__backdrop {
    position: absolute;
    inset: 0;
    width: 848px;
    height: 1200px;
  }
  .certificate__backdrop .field { fill: var(--navy); }
  .certificate__backdrop .sweep { fill: var(--gold); }

  .title,
  .subtitle,
  .presented,
  .statement,
  .label,
  .fill-line {
    position: absolute;
    margin: 0;
  }
  .title {
    left: 74px;
    top: 82px;
    font-size: 94px;
    font-weight: 700;
    line-height: 1;
    letter-spacing: -2px;
  }
  .subtitle {
    left: 76px;
    top: 178px;
    font-size: 51px;
    font-weight: 700;
    line-height: 1;
    letter-spacing: -1px;
  }
  .presented {
    left: 70px;
    top: 331px;
    font-size: 38px;
    font-weight: 300;
    line-height: 1;
  }
  .statement {
    left: 70px;
    top: 523px;
    width: 600px;
    font-size: 23px;
    font-weight: 400;
    line-height: 40px;
    letter-spacing: -0.2px;
  }
  .label {
    font-size: 23px;
    font-weight: 400;
    line-height: 1;
  }
  .label--start { left: 70px; top: 731px; }
  .label--date  { left: 76px; top: 1022px; }

  .fill-line {
    height: 0;
    border-top: 2px dotted var(--rule);
  }
  .fill-line--name   { left: 70px; top: 482px; width: 592px; }
  .fill-line--number { left: 70px; top: 708px; width: 318px; }
  .fill-line--start  { left: 70px; top: 820px; width: 318px; }
  .fill-line--date   { left: 74px; top: 1008px; width: 304px; }

  .issuer {
    position: absolute;
    left: 585px;
    top: 1070px;
    width: 233px;
    height: 88px;
    box-sizing: border-box;
    border: 1px solid var(--navy);
    background: var(--navy);
    outline: 1px solid var(--paper);
    outline-offset: -3px;
    display: flex;
    align-items: center;
    gap: 12px;
    padding: 0 10px 0 8px;
  }
  .issuer__mark {
    width: 64px;
    height: 72px;
    background: var(--paper);
    flex: none;
  }
  .issuer__name {
    font-size: 15px;
    font-weight: 500;
    line-height: 18px;
    color: var(--ink-light);
    text-transform: uppercase;
  }
</style>
</head>
<body>
  <main class="certificate">
    <svg class="certificate__backdrop" viewBox="0 0 848 1200" aria-hidden="true">
      <path class="sweep" d="M804,0 L848,0 L848,430 C848,760 650,1020 383,1200 L294,1200 C560,1020 804,760 804,430 Z"/>
      <path class="field" d="M0,0 H778 V410 C778,740 540,1010 236,1200 H0 Z"/>
    </svg>

    <h1 class="title">CERTIFICATE</h1>
    <p class="subtitle">OF MEMBERSHIP</p>

    <p class="presented">PRESENTED TO</p>
    <div class="fill-line fill-line--name"></div>

    <p class="statement">This is to certify that person stated above was admitted as an official member of BRVO Service Excellence Institute, with membership no:</p>
    <div class="fill-line fill-line--number"></div>

    <p class="label label--start">started from</p>
    <div class="fill-line fill-line--start"></div>

    <div class="fill-line fill-line--date"></div>
    <p class="label label--date">Date</p>

    <div class="issuer">
      <div class="issuer__mark"></div>
      <div class="issuer__name">BRVO Service<br>Excellence<br>Institute</div>
    </div>
  </main>
</body>
</html>
```